New Website for Crime Scene Cleaner required

I need someone to create a complete new website and can set up SEO for me through the Website Designer or a third party for me. I have Logo that i will upload shortly once finalized for the website. I have domain names already but will need to be registered by the winner(i can supply the details I have received from HostMarlo). I am looking for a website that stands out but is simple and elegant, easy to navigate and use yet not boring. Using information provided by me for wording to create it as a stand out website. in total i am looking at 5-7 pages (About/Home, Fire & Smoke Restoration, Water Restoration/Mould Remediation, Crime Scene Cleaners, Methamphetamine Remediation/ Testing Services, Hoarding & Squalor Cleaning, Contact Us/Testimonials)This will be a start to finish project. I would like assistance to have it set up user friendly on mobile devices etc or refer a third party who can assist. Must be able to provide ongoing support when required by myself if the successful winner (i understand this will be an additional fee if required in the future).
You will also require to assist me with the email set up for the website so that it is fully functional or provide a third party who can.
To gain some information about the business you can visit my old website at www.pelbrookcove.com.au and welcome to use some of the wording from there for your entry.
It's been 14yrs since i've had a website made from me so suggestions are welcome if not mentioned in the scope as I want the website to be great.

I have uploaded 2 Logo's and a 3D Logo will come through shortly.

Target Market(s)

People affected by a traumatic event in their lives needing assistance by professionals who are understanding and professionally trained

Coding

Coded - Design and coding required

Requirements
Must have
• *** Please note that correct wording for pages will only be supplied upon a successful winner for the finalization of the project.

I have domain names already but will need to be registered by the winner(i can supply the details I have received from HostMarlo).
Nice to have
• the feeling that we care because we do and that we are passionate for what we do.

```html
<!DOCTYPE html>
<html lang="en">
<head>
<meta charset="utf-8">
<title>Calmfield Decon – Crime Scene &amp; Home Cleanup</title>
<link href="https://fonts.googleapis.com/css2?family=Anton&family=Poppins:wght@300;400;500;600&display=swap" rel="stylesheet">
<style>
:root{
  --navy:#0f2a33;
  --navy-2:#123039;
  --orange:#f26b1d;
  --orange-deep:#e2531a;
  --peach:#fdf0e8;
  --text:#1d2a30;
  --muted:#6f7779;
  --white:#ffffff;
}
*{box-sizing:border-box;margin:0;padding:0}
html,body{width:1200px;height:5333px;overflow:hidden}
body{position:relative;font-family:'Poppins',sans-serif;color:var(--text);background:var(--white)}
.abs{position:absolute}
.photo{position:absolute;display:block}

/* header */
.site-header{position:absolute;left:0;top:0;width:1200px;height:108px;background:var(--navy)}
.brand{position:absolute;left:161px;top:30px;display:flex;align-items:center;gap:8px;color:var(--orange);font-weight:600;font-size:15px;letter-spacing:.5px}
.brand-dot{width:14px;height:14px;background:var(--orange);border-radius:50%}
.contact-chip{position:absolute;top:22px;display:flex;gap:12px;align-items:flex-start;color:var(--white)}
.contact-chip small{display:block;color:var(--orange);font-size:10px}
.contact-chip .big{font-size:19px;font-weight:500}
.contact-chip .mid{font-size:12px}
.main-nav{position:absolute;left:149px;top:87px;width:900px;height:41px;background:var(--orange);z-index:3;box-shadow:0 6px 12px rgba(0,0,0,.2)}
.main-nav a{position:absolute;top:0;height:41px;line-height:41px;font-size:11.5px;color:var(--white);text-decoration:none;white-space:nowrap}
.main-nav a.active{background:var(--orange-deep);padding:0 18px;left:21px}

/* hero */
.hero{position:absolute;left:0;top:108px;width:1200px;height:606px;background:linear-gradient(90deg,#d9dcdc 0%,#9fa4a6 45%,#4b4c4b 70%,#2a2726 100%)}
.hero-tag{position:absolute;left:161px;top:269px;width:207px;height:33px;line-height:33px;background:var(--navy);color:var(--white);font-family:'Anton',sans-serif;font-size:13px;letter-spacing:.5px;padding-left:20px}
.hero-title{position:absolute;left:161px;top:318px;font-family:'Anton',sans-serif;font-weight:400;font-size:50px;line-height:58px;color:#141414;white-space:nowrap}
.hero-sub{position:absolute;left:161px;top:448px;font-size:32px;color:var(--orange);font-weight:300}
.hero-sub b{font-weight:600}
.btn{position:absolute;background:var(--orange);color:var(--white);font-size:13px;font-weight:500;text-align:center;border-radius:6px;text-transform:uppercase}
.slider-arrow{position:absolute;top:368px;width:40px;height:40px;border-radius:50%;background:rgba(60,60,60,.55);display:flex;align-items:center;justify-content:center}
.thumb{position:absolute;top:677px;width:73px;height:68px;border:3px solid var(--white)}

/* welcome */
.welcome{position:absolute;left:0;top:714px;width:1200px;height:466px;background:var(--navy)}
.center{position:absolute;left:0;width:1200px;text-align:center}
.section-title{font-size:32px;color:var(--orange-deep);font-weight:500;text-transform:uppercase;letter-spacing:.5px}
.welcome p{color:#d7dfe1;font-size:11.5px;line-height:20px}

/* services */
.peach{position:absolute;background:var(--peach);height:300px}
.svc-img{position:absolute;width:401px;height:300px;border-radius:0 24px 0 24px}
.svc-icon{position:absolute;width:70px;height:70px;border-radius:12px;background:linear-gradient(160deg,#f68a3c,#e8541b);display:flex;align-items:center;justify-content:center}
.svc-title{position:absolute;font-size:25px;line-height:31px;font-weight:500;color:var(--text)}
.svc-text{position:absolute;width:290px;font-size:11.5px;line-height:20px;color:var(--muted)}
.read-more{position:absolute;font-size:12px;color:var(--orange)}

/* emergency */
.call-circle{position:absolute;width:66px;height:66px;border-radius:50%;background:var(--orange);border:6px solid #fde3d3;display:flex;align-items:center;justify-content:center}

/* testimonials */
.testimonials{position:absolute;left:0;top:3843px;width:1200px;height:493px;background:var(--peach)}
.t-card{position:absolute;left:194px;top:4014px;width:489px;height:322px;background:var(--white)}
.t-quote{position:absolute;left:242px;top:4061px;width:318px;font-size:11.5px;line-height:22.5px;color:var(--muted)}
.t-label{position:absolute;left:548px;top:4268px;width:381px;height:68px;background:var(--orange);color:var(--white);text-align:center;padding-top:14px}

/* contact */
.field{position:absolute;left:583px;width:373px;height:35px;border:1px solid #d9d9d9;font-size:10px;color:#999;padding:11px 14px;background:var(--white)}
.band{position:absolute;left:0;top:4961px;width:1200px;height:65px;background:var(--orange)}

/* footer */
.site-footer{position:absolute;left:0;top:5026px;width:1200px;height:307px;background:var(--navy)}
.f-head{position:absolute;top:5070px;font-size:15px;color:var(--orange)}
.f-list{position:absolute;top:5124px;list-style:none;font-size:11px;line-height:22px;color:#c9d2d4}
.f-list li::before{content:"";display:inline-block;width:5px;height:5px;border-radius:50%;background:var(--orange);margin-right:14px;vertical-align:middle}
.f-contact{position:absolute;left:821px;font-size:11px;color:#c9d2d4;display:flex;gap:12px;line-height:18px}
</style>
</head>
<body>

<header class="site-header">
  <div class="brand"><span class="brand-dot"></span>CALMFIELD DECON</div>
  <div class="contact-chip" style="left:600px">
    <svg width="28" height="28" viewBox="0 0 24 24"><path d="M6.6 10.8a15 15 0 006.6 6.6l2.2-2.2a1 1 0 011-.25 11 11 0 003.6.6 1 1 0 011 1V20a1 1 0 01-1 1A17 17 0 013 4a1 1 0 011-1h3.5a1 1 0 011 1 11 11 0 00.6 3.6 1 1 0 01-.25 1z" fill="none" stroke="#f26b1d" stroke-width="1.6"/></svg>
    <div><small>Phone *</small><span class="big">0400 555 218</span></div>
  </div>
  <div class="contact-chip" style="left:797px">
    <svg width="32" height="26" viewBox="0 0 32 26"><rect x="2" y="3" width="28" height="20" rx="2" fill="none" stroke="#f26b1d" stroke-width="1.8"/><path d="M2 4l14 11L30 4" fill="none" stroke="#f26b1d" stroke-width="1.8"/></svg>
    <div><small>Email Us *</small><span class="mid">hello@calmfielddecon.com.au</span></div>
  </div>
</header>

<nav class="main-nav">
  <a class="active">Home</a>
  <a style="left:101px">Fire &amp; Smoke Restoration</a>
  <a style="left:265px">Water Restoration</a>
  <a style="left:387px">Crime Scene Cleaners</a>
  <a style="left:530px">Testing Services</a>
  <a style="left:639px">Hoarding &amp; Squalor Cleaning</a>
  <a style="left:823px">Contact Us</a>
</nav>

<section class="hero" role="img" aria-label="Firefighter spraying water over a smoking, burnt-out house">
</section>
<div class="hero-tag">Fire &amp; Smoke Restoration</div>
<h1 class="hero-title">24/7 CRIME SCENE &amp;<br>HOME CLEANUP</h1>
<p class="hero-sub">We're Here To <b>Help.</b></p>
<div class="btn" style="left:161px;top:511px;width:143px;height:40px;line-height:40px;border-radius:8px">Contact Us</div>
<div class="slider-arrow" style="left:62px"><svg width="14" height="14" viewBox="0 0 14 14"><path d="M9 2L4 7l5 5" stroke="#fff" stroke-width="2" fill="none"/></svg></div>
<div class="slider-arrow" style="left:1104px"><svg width="14" height="14" viewBox="0 0 14 14"><path d="M5 2l5 5-5 5" stroke="#fff" stroke-width="2" fill="none"/></svg></div>
<div class="thumb" role="img" aria-label="Crime scene technician thumbnail" style="left:490px;background:linear-gradient(135deg,#c9c4b8,#5b5a55)"></div>
<div class="thumb" role="img" aria-label="Firefighter thumbnail" style="left:563px;border-color:var(--orange);background:linear-gradient(135deg,#e4e5e5,#505352)"></div>
<div class="thumb" role="img" aria-label="Crime scene tape thumbnail" style="left:637px;background:linear-gradient(135deg,#2d3a80,#c8a92a)"></div>

<section class="welcome">
  <div class="center" style="top:100px;color:#fff;font-size:14px">Welcome To</div>
  <div class="center section-title" style="top:132px">Calmfield Decon</div>
  <div class="center" style="top:186px"><p style="width:352px;margin:0 auto">Lorem Ipsum is simply dummy text of the printing typesetti industry. Lorem Ipsum has been the industry's standard dummy text ever since the when.</p></div>
  <div class="center" style="top:261px"><p style="width:352px;margin:0 auto">Lorem Ipsum is simply dummy text of the printing typesetti industry. Lorem Ipsum has been the industry's standard dummy text ever since the 1500s, when an unknown printer took a the galley of type and scrambled it to.</p></div>
  <div class="btn" style="left:530px;top:352px;width:140px;height:39px;line-height:39px;border-radius:10px">Know More</div>
</section>

<div class="center section-title" style="top:1252px">Services We Provide</div>
<div class="center" style="top:1300px;font-size:11.5px;line-height:22px;color:var(--muted)">Lorem Ipsum is simply dummy text of the printing typesetti industry the<br>Lorem Ipsum has been the industry.</div>

<!-- row 1 -->
<div class="peach" style="left:0;top:1463px;width:526px"></div>
<div class="svc-img" role="img" aria-label="Fire-damaged kitchen with charred walls" style="left:199px;top:1395px;background:linear-gradient(135deg,#6b5f55,#231d19)"></div>
<div class="svc-icon" style="left:697px;top:1426px"><svg width="36" height="36" viewBox="0 0 36 36" fill="none" stroke="#fff" stroke-width="2"><path d="M18 4c3 6-4 8-4 14a4 4 0 008 0c0-3-2-4-2-4 4 2 6 6 6 9a8 8 0 01-16 0c0-9 8-11 8-19z"/><path d="M6 32h24"/></svg></div>
<div class="svc-title" style="left:697px;top:1505px">Fire &amp; Smoke<br>Restoration</div>
<div class="svc-text" style="left:697px;top:1576px">Lorem Ipsum is simply dummy text of the printing typesetti industry. Lorem Ipsum has been the industry's standard dummy text ever.</div>
<div class="read-more" style="left:697px;top:1648px">Read More ▸</div>

<!-- row 2 -->
<div class="peach" style="left:675px;top:1907px;width:525px"></div>
<div class="svc-img" role="img" aria-label="Flooded living room with water on the floor" style="left:600px;top:1839px;background:linear-gradient(135deg,#e6e7e3,#8c8f85)"></div>
<div class="svc-icon" style="left:209px;top:1870px"><svg width="36" height="36" viewBox="0 0 36 36" fill="none" stroke="#fff" stroke-width="2"><path d="M6 12h24M18 6v6M10 12v8h16v-8M18 20v4"/><path d="M18 26c-2 3-2 5 0 5s2-2 0-5z"/></svg></div>
<div class="svc-title" style="left:209px;top:1949px">Water Restoration/<br>Mould Remediation</div>
<div class="svc-text" style="left:209px;top:2020px">Lorem Ipsum is simply dummy text of the printing typesetti industry. Lorem Ipsum has been the industry's standard dummy text ever.</div>
<div class="read-more" style="left:209px;top:2092px">Read More ▸</div>

<!-- row 3 -->
<div class="peach" style="left:0;top:2350px;width:526px"></div>
<div class="svc-img" role="img" aria-label="Gloved hand behind yellow crime scene tape" style="left:199px;top:2282px;background:linear-gradient(135deg,#e9e9e9,#5a7fb3 55%,#e5c321)"></div>
<div class="svc-icon" style="left:697px;top:2313px"><svg width="36" height="36" viewBox="0 0 36 36" fill="none" stroke="#fff" stroke-width="2"><rect x="5" y="8" width="26" height="18"/><path d="M5 8l26 18M31 8L5 26M8 26v4M28 26v4"/></svg></div>
<div class="svc-title" style="left:697px;top:2392px">Crime Scene<br>Cleaners</div>
<div class="svc-text" style="left:697px;top:2463px">Lorem Ipsum is simply dummy text of the printing typesetti industry. Lorem Ipsum has been the industry's standard dummy text ever.</div>
<div class="read-more" style="left:697px;top:2535px">Read More ▸</div>

<!-- row 4 -->
<div class="peach" style="left:675px;top:2795px;width:525px"></div>
<div class="svc-img" role="img" aria-label="Gloved hand holding a small bag of crystals" style="left:600px;top:2727px;background:linear-gradient(135deg,#3a5fc0,#0d1a3a)"></div>
<div class="svc-icon" style="left:216px;top:2758px"><svg width="36" height="36" viewBox="0 0 36 36" fill="none" stroke="#fff" stroke-width="2"><path d="M18 4v10M12 10l6 6 6-6M8 30l4-10h12l4 10zM18 20v10"/></svg></div>
<div class="svc-title" style="left:216px;top:2837px">Methamphetamine<br>Remediation/ Testing<br>Services</div>
<div class="svc-text" style="left:216px;top:2940px">Lorem Ipsum is simply dummy text of the printing typesetti industry Lorem Ipsum has.</div>
<div class="read-more" style="left:216px;top:2990px">Read More ▸</div>

<!-- row 5 -->
<div class="peach" style="left:0;top:3238px;width:526px"></div>
<div class="svc-img" role="img" aria-label="Cluttered room filled with hoarded belongings" style="left:199px;top:3170px;background:linear-gradient(135deg,#b86a4c,#50463d)"></div>
<div class="svc-icon" style="left:697px;top:3201px"><svg width="36" height="36" viewBox="0 0 36 36" fill="none" stroke="#fff" stroke-width="2"><rect x="5" y="6" width="26" height="24"/><path d="M5 14h26M11 20h6v6h-6zM21 20h6"/></svg></div>
<div class="svc-title" style="left:697px;top:3280px">Hoarding &amp; Squalor<br>Cleaning</div>
<div class="svc-text" style="left:697px;top:3351px">Lorem Ipsum is simply dummy text of the printing typesetti industry. Lorem Ipsum has been the industry's standard dummy text ever.</div>
<div class="read-more" style="left:697px;top:3423px">Read More ▸</div>

<!-- emergency -->
<div class="center" style="top:3610px;font-size:27px;font-weight:500">Have An Any Emergency ?</div>
<div class="center" style="top:3655px;font-size:12px">Cleaning &amp; Property Maintenance Specialist</div>
<div class="abs" style="right:646px;top:3716px;font-size:20px;font-weight:500;color:#e23a1e">Call Us Today :</div>
<div class="call-circle" style="left:573px;top:3698px"><svg width="26" height="26" viewBox="0 0 24 24"><path d="M6.6 10.8a15 15 0 006.6 6.6l2.2-2.2a1 1 0 011-.25 11 11 0 003.6.6 1 1 0 011 1V20a1 1 0 01-1 1A17 17 0 013 4a1 1 0 011-1h3.5a1 1 0 011 1 11 11 0 00.6 3.6 1 1 0 01-.25 1z" fill="#fff"/></svg></div>
<div class="abs" style="left:654px;top:3716px;font-size:20px;font-weight:500;color:#e23a1e">0400 555 218</div>

<!-- testimonials -->
<section class="testimonials"></section>
<div class="center" style="top:3902px;font-size:13px">Testimonials</div>
<div class="center section-title" style="top:3926px">Thank You For Trusting Us</div>
<div class="t-card"></div>
<p class="t-quote">" I have used Calmfield Decon cleaners for over a year now and I have always been more than happy with their work. They are professional, quick and fairly priced. I would recommend their team to anyone and have done so. Thanks to Calmfield Decon I know that the property will be cleaned properly and I am confident they will do the same for you. Thank you. "</p>
<div class="abs" style="left:243px;top:4256px;width:32px;height:32px;border-radius:50%;background:#fbd1b5"></div>
<div class="abs" style="left:288px;top:4256px;width:32px;height:32px;border-radius:50%;border:2px solid #fbc7a4;display:flex;align-items:center;justify-content:center"><svg width="10" height="12" viewBox="0 0 10 12"><path d="M2 1l5 5-5 5" stroke="#f26b1d" stroke-width="1.6" fill="none"/></svg></div>
<div class="photo" role="img" aria-label="Property manager working at a laptop" style="left:621px;top:4059px;width:308px;height:215px;background:linear-gradient(135deg,#f1efec,#b9b2a8)"></div>
<div class="t-label"><div style="font-size:13px;font-weight:500">Renata Kovac, Property Manager</div><div style="font-size:11px">Harbourline Property, Ashvale</div></div>

<!-- contact -->
<div class="photo" role="img" aria-label="Support agent with headset pointing toward the form" style="left:207px;top:4397px;width:331px;height:564px;background:linear-gradient(180deg,#eef0f2,#c9ccd2)"></div>
<div class="abs section-title" style="left:583px;width:373px;top:4406px;text-align:center">Contact Us</div>
<div class="abs" style="left:583px;width:373px;top:4456px;text-align:center;font-size:12px;color:var(--muted)">If you have an any Question for contact us Today :</div>
<div class="abs" style="left:583px;width:373px;top:4496px;text-align:center;font-size:19px;font-weight:500">24/7 Available</div>
<div class="field" style="top:4548px;border-color:var(--orange)">Name *</div>
<div class="field" style="top:4597px">Email *</div>
<div class="field" style="top:4645px">Phone *</div>
<div class="field" style="top:4693px">Services *<span style="float:right;color:var(--orange)">▾</span></div>
<div class="field" style="top:4738px;height:89px">Message *</div>
<div class="btn" style="left:710px;top:4841px;width:118px;height:40px;line-height:40px;border-radius:8px">Submit</div>

<div class="band">
  <div class="abs" style="right:652px;top:20px;color:#fff;font-size:16px">Emergency and After Hours :</div>
  <div class="abs" style="left:579px;top:11px;width:42px;height:42px;border-radius:50%;border:2px solid #fff;display:flex;align-items:center;justify-content:center"><svg width="20" height="20" viewBox="0 0 24 24"><path d="M6.6 10.8a15 15 0 006.6 6.6l2.2-2.2a1 1 0 011-.25 11 11 0 003.6.6 1 1 0 011 1V20a1 1 0 01-1 1A17 17 0 013 4a1 1 0 011-1h3.5a1 1 0 011 1 11 11 0 00.6 3.6 1 1 0 01-.25 1z" fill="#fff"/></svg></div>
  <div class="abs" style="left:646px;top:16px;color:#fff;font-size:22px;font-weight:500">0400 555 218</div>
</div>

<footer class="site-footer"></footer>
<div class="abs" style="left:176px;top:5120px;width:186px;text-align:center;color:var(--orange);font-size:16px;font-weight:600;letter-spacing:.5px">CALMFIELD DECON</div>
<div class="abs" style="left:253px;top:5198px;width:32px;height:32px;border-radius:50%;background:var(--orange)"></div>

<div class="f-head" style="left:418px">QuickLinks</div>
<ul class="f-list" style="left:418px"><li>Home</li><li>About Us</li><li>Testimonials</li><li>Contact Us</li><li>Faq</li></ul>
<div class="f-head" style="left:596px">What We Do</div>
<ul class="f-list" style="left:596px"><li>Fire &amp; Smoke Restoration</li><li>Water Restoration</li><li>Crime Scene Cleaners</li><li>Testing Services</li><li>Hoarding &amp; Squalor Cleaning</li></ul>
<div class="f-head" style="left:821px">Contact Info</div>
<div class="f-contact" style="top:5106px"><svg width="18" height="20" viewBox="0 0 18 20"><path d="M9 1a6 6 0 016 6c0 5-6 12-6 12S3 12 3 7a6 6 0 016-6z" fill="none" stroke="#f26b1d" stroke-width="1.8"/><circle cx="9" cy="7" r="2" fill="#f26b1d"/></svg><span>12 Wren Street<br>Ashvale QLD 4300</span></div>
<div class="f-contact" style="top:5174px"><svg width="18" height="14" viewBox="0 0 18 14"><rect x="1" y="1" width="16" height="12" fill="#f26b1d"/><path d="M1 1l8 6 8-6" stroke="#0f2a33" stroke-width="1.4" fill="none"/></svg><span>hello@calmfielddecon.com.au</span></div>
<div class="f-contact" style="top:5213px"><svg width="18" height="18" viewBox="0 0 24 24"><path d="M6.6 10.8a15 15 0 006.6 6.6l2.2-2.2a1 1 0 011-.25 11 11 0 003.6.6 1 1 0 011 1V20a1 1 0 01-1 1A17 17 0 013 4a1 1 0 011-1h3.5a1 1 0 011 1 11 11 0 00.6 3.6 1 1 0 01-.25 1z" fill="#f26b1d"/></svg><span style="font-size:12px;color:#fff">0400 555 218</span></div>

<div class="center" style="top:5296px;font-size:10px;color:#9aa5a8"><span style="color:var(--orange)">©CALMFIELD DECON SERVICES</span> – 2020 All rights reserved</div>

</body>
</html>
```